New look and feel for a Website, mobile design, desktop design

We do a redesign of the website kolvany.com. We expect the designer to come up with ideas about a new look AND feel.
Starting point of the designers considerations should be the mobile design. Even though we are not creating a mobile App, the designer should think of it as one regarding design and usability. Using responsive design technology, we will shift from the mobile design to the desktop design and likewise. So the designer is supposed to come up with a solution for that as well.
What we expect
- definition of single design-elements that can be used in various places
- creation of a mobile design for all different types of pages
- creation of a desktop design for all different types of pages
Find a detailed description in the redesign-specification.

Target Market(s)

Germany, Austria, Switzerland

Industry/Entity Type

Residential Construction

Number of Pages Required

5+ page

Font styles to use
Other font styles liked:
• Open Sans

Colors

Designer to choose colors to be used in the design.

Requirements
Must have
• - mobile design concept
• - desktop design concept
• More information see document "Redesign-kolvany-specification.doc"

```html
<!DOCTYPE html>
<html lang="en">
<head>
<meta charset="utf-8">
<title>Kolvany – Bathroom Renovation · Desktop and Mobile</title>
<link rel="stylesheet" href="https://fonts.googleapis.com/css2?family=Open+Sans:wght@400;600;700;800&display=swap">
<style>
  :root{
    --navy:#0f4566;
    --orange:#ea6f12;
    --sky:#1a7bbf;
    --side:#39434d;
    --page:#ffffff;
    --text:#2b3a44;
    --muted:#6f7d86;
    --line:#dde3e7;
    --stage-top:#d3e3e8;
    --stage-bottom:#d7d9db;
  }
  *{box-sizing:border-box;margin:0;padding:0}
  html,body{width:1200px;height:1000px;overflow:hidden}
  body{font-family:"Open Sans",Arial,sans-serif;background:linear-gradient(var(--stage-top),var(--stage-bottom));color:var(--text);position:relative}

  .btn{display:inline-block;font-weight:700;text-transform:uppercase;letter-spacing:.4px;color:#fff;font-size:11px;padding:8px 16px;white-space:nowrap;text-align:center}
  .btn-orange{background:var(--orange)}
  .btn-navy{background:var(--navy)}
  .label{color:var(--orange);font-weight:600}
  .brand{display:flex;align-items:center;gap:10px}
  .brand-mark{border-radius:50%;background:var(--sky);flex:none}
  .brand-name{font-weight:600;color:var(--navy)}

  /* ===== desktop page ===== */
  .desktop{position:absolute;left:36px;top:112px;width:960px;height:942px;transform:scale(.82);transform-origin:0 0;background:var(--side);box-shadow:0 14px 40px rgba(0,0,0,.25)}
  .site{width:864px;height:942px;margin:0 auto;background:var(--page)}
  .wrap{padding:0 40px}
  .header{height:100px;display:flex;justify-content:space-between;align-items:center}
  .desktop .brand-mark{width:22px;height:22px}
  .desktop .brand-name{font-size:26px}
  .header-info{text-align:right}
  .header-top{display:flex;justify-content:flex-end;align-items:center;gap:18px;font-size:12px}
  .email{color:var(--navy)}
  .hotlines{margin-top:14px;font-size:12px;font-weight:700;color:var(--navy);display:flex;gap:14px;justify-content:flex-end;align-items:center}
  .hotlines .label{display:flex;align-items:center;gap:6px}
  .nav{background:var(--navy);height:36px}
  .nav ul{list-style:none;display:flex;height:36px;padding:0 40px}
  .nav li{color:#fff;font-size:12px;font-weight:600;padding:0 11px;line-height:36px;white-space:nowrap}
  .nav li.active{background:var(--orange)}

  .hero{display:flex;gap:18px;margin-top:24px}
  .slider{position:relative;width:530px;height:300px;background:linear-gradient(135deg,#8e9498 0%,#c9cdcf 40%,#7d8387 70%,#3e4347 100%)}
  .slide-badge{position:absolute;left:110px;top:40px;width:190px;height:190px;border-radius:50%;background:rgba(255,255,255,.55);display:flex;flex-direction:column;align-items:center;justify-content:center;text-align:center}
  .slide-kicker{font-size:11px;font-weight:700;letter-spacing:1px;color:#3b4a54}
  .slide-title{font-size:19px;font-weight:600;color:var(--text);margin-top:4px;line-height:1.3}
  .slide-badge .btn{margin-top:28px}
  .slider-next{position:absolute;right:16px;top:135px}
  .callbox{flex:1;background:#fff;box-shadow:0 0 0 1px var(--line),0 4px 10px rgba(0,0,0,.08);padding-bottom:14px}
  .callbox-head{background:var(--orange);color:#fff;text-align:center;padding:12px 0 30px;clip-path:polygon(0 0,100% 0,100% 70%,50% 100%,0 70%)}
  .callbox-head h2{font-size:21px;font-weight:600;line-height:1.3}
  .callbox-head p{font-size:11px;font-weight:700;letter-spacing:.4px}
  .call-list{list-style:none;padding:16px 20px 6px}
  .call-list li{display:flex;align-items:center;gap:14px;font-size:14px;font-weight:700;color:var(--navy);margin-bottom:12px;white-space:nowrap}
  .call-list li.highlight{color:var(--orange)}
  .callbox .btn{display:block;margin:8px 14px 0;padding:9px 0}

  .band{margin-top:22px;height:70px;background:linear-gradient(90deg,#4e575e,#727b81 50%,#4e575e);color:#fff;text-align:center;padding-top:12px}
  .band h3{font-size:22px;font-weight:600;line-height:1.3}
  .band p{font-size:12px;font-weight:600}

  .tiles{display:flex;gap:18px;margin-top:20px}
  .tile{flex:1;height:130px;color:#fff;padding:18px 22px}
  .tile-orange{background:var(--orange)}
  .tile-navy{background:var(--navy)}
  .tile-area{background:#fff;box-shadow:0 0 0 1px var(--line);padding:0;color:var(--text)}
  .tile-big{font-size:42px;font-weight:800;line-height:1}
  .tile-big sup{font-size:18px}
  .tile-text{font-size:13px;font-weight:600;margin-top:10px}
  .tile-area h4{background:var(--sky);color:#fff;font-size:15px;font-weight:600;text-align:center;padding:10px 0}
  .search{display:flex;margin:22px 16px 0}
  .search-field{flex:1;border:1px solid var(--line);font-size:12px;color:var(--muted);padding:8px 10px;white-space:nowrap}

  .media{display:flex;gap:18px;margin-top:20px}
  .video{position:relative;width:380px;height:190px;background:linear-gradient(135deg,#3d3a36,#8a6a4a 55%,#4a4744)}
  .video svg{position:absolute;left:50%;top:50%;transform:translate(-50%,-50%)}
  .recs{flex:1}
  .recs-head{display:flex;justify-content:space-between;align-items:baseline;font-size:14px;font-weight:700;color:var(--navy);border-bottom:2px solid var(--navy);padding-bottom:6px}
  .recs-head span{font-size:11px;color:var(--orange);font-weight:600}
  .cards{display:flex;gap:10px;margin-top:12px}
  .card{flex:1;text-align:center;font-size:11px;font-weight:600;white-space:nowrap}
  .card-img{height:100px;margin-bottom:8px}
  .card .btn{display:block;margin-top:8px;padding:6px 0;font-size:10px}
  .img-shower{background:linear-gradient(#e7eaec,#b9c0c4)}
  .img-tub{background:linear-gradient(#eef0f1,#c4cacd)}
  .img-panel{background:linear-gradient(#d8c2b8,#a5544a)}

  /* ===== mobile page ===== */
  .mobile{position:absolute;left:862px;top:70px;width:304px;height:860px;background:var(--page);box-shadow:0 14px 40px rgba(0,0,0,.25);overflow:hidden}
  .m-topbar{background:var(--navy);color:#fff;font-size:11px;font-weight:600;height:26px;display:flex;align-items:center;justify-content:center;gap:6px}
  .m-topbar .label{color:#fff}
  .m-header{height:52px;display:flex;justify-content:space-between;align-items:center;padding:0 14px}
  .mobile .brand{gap:7px}
  .mobile .brand-mark{width:16px;height:16px}
  .mobile .brand-name{font-size:19px}
  .m-menu{display:flex;flex-direction:column;gap:4px}
  .m-menu span{width:22px;height:3px;background:var(--navy)}
  .m-career{display:block;margin:0 14px;padding:8px 0;font-size:11px}
  .m-hero{position:relative;margin:10px 14px 0;height:170px;background:linear-gradient(135deg,#8e9498 0%,#c9cdcf 40%,#7d8387 70%,#3e4347 100%);display:flex;align-items:center;justify-content:center}
  .m-badge{width:140px;height:140px;border-radius:50%;background:rgba(255,255,255,.55);display:flex;flex-direction:column;align-items:center;justify-content:center;text-align:center}
  .m-badge .slide-kicker{font-size:9px}
  .m-badge .slide-title{font-size:14px;margin-top:2px}
  .m-badge .btn{margin-top:12px;font-size:9px;padding:6px 10px}
  .m-call{margin:10px 14px 0;box-shadow:0 0 0 1px var(--line),0 3px 8px rgba(0,0,0,.08);padding-bottom:10px}
  .m-call .callbox-head{padding:9px 0 22px}
  .m-call .callbox-head h2{font-size:17px}
  .m-call .callbox-head p{font-size:10px}
  .m-call .call-list{padding:12px 18px 2px}
  .m-call .call-list li{font-size:13px;margin-bottom:9px}
  .m-call .btn{display:block;margin:6px 12px 0;padding:8px 0;font-size:10px}
  .m-band{margin:10px 14px 0;height:54px;background:linear-gradient(90deg,#4e575e,#727b81 50%,#4e575e);color:#fff;text-align:center;padding-top:8px}
  .m-band h3{font-size:16px;font-weight:600;line-height:1.3}
  .m-band p{font-size:9px;font-weight:600}
  .m-tiles{display:flex;gap:10px;margin:10px 14px 0}
  .m-tiles .tile{height:84px;padding:10px 12px}
  .m-tiles .tile-big{font-size:28px}
  .m-tiles .tile-big sup{font-size:12px}
  .m-tiles .tile-text{font-size:10px;margin-top:6px;line-height:1.35}
  .m-area{margin:10px 14px 0;box-shadow:0 0 0 1px var(--line)}
  .m-area h4{background:var(--sky);color:#fff;font-size:13px;font-weight:600;text-align:center;padding:7px 0}
  .m-area .search{margin:12px 12px 12px}
  .m-area .search-field{font-size:11px;padding:7px 9px}
  .m-area .btn{font-size:10px;padding:8px 12px}
</style>
</head>
<body>

<section class="desktop" aria-label="Desktop design">
  <div class="site">
    <header class="header wrap">
      <div class="brand"><span class="brand-mark"></span><span class="brand-name">kolvany</span></div>
      <div class="header-info">
        <div class="header-top">
          <span><span class="label">Email Us:</span> <span class="email">info@kolvany.com</span></span>
          <span class="btn btn-orange">Career at Kolvany</span>
        </div>
        <div class="hotlines">
          <span class="label">Call Us For Free:
            <svg width="12" height="12" viewBox="0 0 24 24"><path fill="#ea6f12" d="M6.6 10.8a15 15 0 006.6 6.6l2.2-2.2a1 1 0 011-.25 11.4 11.4 0 003.6.57 1 1 0 011 1V20a1 1 0 01-1 1A17 17 0 013 4a1 1 0 011-1h3.5a1 1 0 011 1c0 1.25.2 2.45.57 3.57a1 1 0 01-.25 1z"/></svg>
          </span>
          <span>A - 866 - 555 - 0142</span><span>D - 0800 10 20 301</span><span>CH - 0800 30 40 512</span>
        </div>
      </div>
    </header>

    <nav class="nav">
      <ul>
        <li class="active">Home</li><li>About Kolvany</li><li>Bath Solutions</li><li>Bath Information</li><li>Measure Up</li><li>Product Reviews</li><li>Locations</li><li>Press</li>
      </ul>
    </nav>

    <main class="wrap">
      <section class="hero">
        <div class="slider" role="img" aria-label="Photo of a modern renovated bathroom with walk-in shower">
          <div class="slide-badge">
            <span class="slide-kicker">WHIRLPOOL BATHS</span>
            <span class="slide-title">Specialist<br>Companies</span>
            <span class="btn btn-orange">Contact Us</span>
          </div>
          <svg class="slider-next" width="16" height="30" viewBox="0 0 16 30"><path d="M2 2l12 13L2 28" fill="none" stroke="#fff" stroke-width="2"/></svg>
        </div>
        <aside class="callbox">
          <div class="callbox-head">
            <h2>Call now for free</h2>
            <p>MON-FRI 7:30-19:15 CLOCK</p>
          </div>
          <ul class="call-list">
            <li><svg width="24" height="16"><rect width="24" height="16" fill="#d7262e"/><rect y="5.3" width="24" height="5.4" fill="#fff"/></svg>Call Us: 0800 50 60 714</li>
            <li class="highlight"><svg width="24" height="16"><rect width="24" height="5.4" fill="#111"/><rect y="5.3" width="24" height="5.4" fill="#d7262e"/><rect y="10.6" width="24" height="5.4" fill="#f2c200"/></svg>Call Us: 0800 10 20 301</li>
            <li><svg width="24" height="16"><rect width="24" height="16" fill="#d7262e"/><rect x="10" y="3" width="4" height="10" fill="#fff"/><rect x="7" y="6" width="10" height="4" fill="#fff"/></svg>Call Us: 0800 30 40 512</li>
          </ul>
          <span class="btn btn-navy">Request a Quote</span>
          <span class="btn btn-navy">Pre Bath Consultation</span>
        </aside>
      </section>

      <section class="band">
        <h3>A new bath in 24 hours</h3>
        <p>with Kolvany System Solutions for Bathroom Renovation</p>
      </section>

      <section class="tiles">
        <div class="tile tile-orange">
          <div class="tile-big">24<sup>h</sup></div>
          <div class="tile-text">Bathroom renovation done in one day</div>
        </div>
        <div class="tile tile-navy">
          <div class="tile-big">8<sup>th</sup></div>
          <div class="tile-text">Years of quality experience</div>
        </div>
        <div class="tile tile-area">
          <h4>Kolvany in your area</h4>
          <div class="search"><span class="search-field">Enter postcode</span><span class="btn btn-navy">Search</span></div>
        </div>
      </section>

      <section class="media">
        <div class="video" role="img" aria-label="Video still of a bathroom renovation consultation">
          <svg width="50" height="50" viewBox="0 0 50 50"><circle cx="25" cy="25" r="23" fill="rgba(255,255,255,.25)" stroke="#fff" stroke-width="2"/><path d="M20 15l15 10-15 10z" fill="#fff"/></svg>
        </div>
        <div class="recs">
          <div class="recs-head">Recommendations <span>Show all products</span></div>
          <div class="cards">
            <div class="card"><div class="card-img img-shower" role="img" aria-label="Product photo of a walk-in shower"></div>Walk-in shower<span class="btn btn-orange">Details</span></div>
            <div class="card"><div class="card-img img-tub" role="img" aria-label="Product photo of a bathtub converted to shower"></div>Bathtub to shower<span class="btn btn-orange">Details</span></div>
            <div class="card"><div class="card-img img-panel" role="img" aria-label="Product photo of decorative wall panels"></div>Wall panels<span class="btn btn-orange">Details</span></div>
          </div>
        </div>
      </section>
    </main>
  </div>
</section>

<section class="mobile" aria-label="Mobile design">
  <div class="m-topbar"><span class="label">Call Us:</span> A - 866 - 555 - 0142</div>
  <header class="m-header">
    <div class="brand"><span class="brand-mark"></span><span class="brand-name">kolvany</span></div>
    <div class="m-menu" aria-label="Menu"><span></span><span></span><span></span></div>
  </header>
  <span class="btn btn-orange m-career">Career at Kolvany</span>

  <div class="m-hero" role="img" aria-label="Photo of a modern renovated bathroom with walk-in shower">
    <div class="m-badge">
      <span class="slide-kicker">WHIRLPOOL BATHS</span>
      <span class="slide-title">Specialist<br>Companies</span>
      <span class="btn btn-orange">Contact Us</span>
    </div>
  </div>

  <aside class="m-call">
    <div class="callbox-head">
      <h2>Call now for free</h2>
      <p>MON-FRI 7:30-19:15 CLOCK</p>
    </div>
    <ul class="call-list">
      <li><svg width="22" height="15"><rect width="22" height="15" fill="#d7262e"/><rect y="5" width="22" height="5" fill="#fff"/></svg>Call Us: 0800 50 60 714</li>
      <li class="highlight"><svg width="22" height="15"><rect width="22" height="5" fill="#111"/><rect y="5" width="22" height="5" fill="#d7262e"/><rect y="10" width="22" height="5" fill="#f2c200"/></svg>Call Us: 0800 10 20 301</li>
      <li><svg width="22" height="15"><rect width="22" height="15" fill="#d7262e"/><rect x="9" y="3" width="4" height="9" fill="#fff"/><rect x="6.5" y="5.5" width="9" height="4" fill="#fff"/></svg>Call Us: 0800 30 40 512</li>
    </ul>
    <span class="btn btn-navy">Request a Quote</span>
    <span class="btn btn-navy">Pre Bath Consultation</span>
  </aside>

  <section class="m-band">
    <h3>A new bath in 24 hours</h3>
    <p>with Kolvany System Solutions for Bathroom Renovation</p>
  </section>

  <section class="m-tiles">
    <div class="tile tile-orange">
      <div class="tile-big">24<sup>h</sup></div>
      <div class="tile-text">Renovation done in one day</div>
    </div>
    <div class="tile tile-navy">
      <div class="tile-big">8<sup>th</sup></div>
      <div class="tile-text">Years of quality experience</div>
    </div>
  </section>

  <section class="m-area">
    <h4>Kolvany in your area</h4>
    <div class="search"><span class="search-field">Enter postcode</span><span class="btn btn-navy">Search</span></div>
  </section>
</section>

</body>
</html>
```